Tax Preparation flyer for LedgerMint Corp.

My Client would like a one page PDF flyer to promote upcoming tax season in Canada. This firm is affordable and all virtual. I have attached a copy of their logo and a word document with the proposed wording for the flyer. Please feel free to change if you have better suggestions.

Target Market(s)

individuals in canada

Colors
0054AA
0677BA
7BADD7
CADEEF
E8F1F8

```html
<!DOCTYPE html>
<html lang="en">
<head>
<meta charset="utf-8">
<title>LedgerMint Corp. – Tax Season Flyer</title>
<link href="https://fonts.googleapis.com/css2?family=Montserrat:wght@400;600;700&family=Rubik:wght@800&family=Oswald:wght@500&display=swap" rel="stylesheet">
<style>
  :root{
    --navy:#0054AA;
    --blue:#0677BA;
    --sky:#7BADD7;
    --mist:#CADEEF;
    --ice:#E8F1F8;
    --ink:#1b1b22;
    --brand-ink:#2b2d3a;
    --accent:#1f8fd6;
    --card-top:#0a8cff;
    --card-bottom:#6c7bff;
    --card-bottom-deep:#7a78ff;
    --tick:#2bd46a;
    --head-a:#1f6bff;
    --head-b:#4f7cf8;
    --head-c:#9a5ef0;
  }
  *{margin:0;padding:0;box-sizing:border-box}
  html,body{width:849px;height:1200px;overflow:hidden}
  body{font-family:"Montserrat",sans-serif;color:var(--ink)}
  .flyer{position:relative;width:849px;height:1200px;overflow:hidden;
    background:linear-gradient(180deg,#ffffff 0%,#f4f8fd 45%,var(--ice) 75%,#dcebfa 100%)}

  .decor{position:absolute}
  .decor--top{right:0;top:0;width:414px;height:307px;
    background:radial-gradient(ellipse at 75% 30%,rgba(20,200,255,.85) 0%,rgba(120,110,255,.7) 40%,rgba(220,120,255,.35) 65%,rgba(255,255,255,0) 80%)}
  .decor--bottom{left:0;bottom:0;width:370px;height:152px;
    background:radial-gradient(ellipse at 20% 90%,rgba(70,140,255,.85) 0%,rgba(170,110,255,.55) 45%,rgba(255,255,255,0) 75%)}

  .brand{position:absolute;left:43px;top:40px;font-weight:700;font-size:29px;color:var(--brand-ink);letter-spacing:-.5px}
  .brand-ghost{position:absolute;left:100px;top:255px;font-family:"Rubik",sans-serif;font-weight:800;font-size:120px;color:rgba(120,150,190,.07);letter-spacing:-3px;white-space:nowrap}

  .headline{position:absolute;left:40px;top:128px;font-family:"Rubik",sans-serif;font-weight:800;font-size:72px;line-height:85px;letter-spacing:-3px;
    background:linear-gradient(100deg,var(--head-a) 0%,var(--head-b) 45%,var(--head-c) 100%);-webkit-background-clip:text;background-clip:text;color:transparent}

  .intro{position:absolute;left:41px;width:780px;font-size:16.4px;line-height:20.7px;letter-spacing:.05px}
  .intro b{font-weight:700}
  .intro--lead{top:398px}
  .intro--meet{top:501px}

  .pricing-title{position:absolute;left:0;width:849px;top:549px;text-align:center;font-weight:700;font-size:25px;color:var(--accent)}

  .plan{position:absolute;color:#fff;background:linear-gradient(180deg,var(--card-top) 0%,var(--card-bottom) 100%)}
  .plan--basic{left:46px;top:630px;width:252px;height:336px;border-radius:9px 0 0 9px}
  .plan--business{left:549px;top:630px;width:252px;height:336px;border-radius:0 9px 9px 0}
  .plan--premium{left:296px;top:589px;width:253px;height:401px;border-radius:10px;border:5px solid #fff;
    background:linear-gradient(180deg,var(--card-top) 0%,var(--card-bottom-deep) 100%);box-shadow:0 2px 8px rgba(40,80,160,.12)}
  .plan-name{position:absolute;left:23px;font-weight:600;font-size:20px}
  .plan-price{position:absolute;left:22px;font-family:"Oswald",sans-serif;font-weight:500;font-size:34px}
  .plan--basic .plan-name,.plan--business .plan-name{top:12px}
  .plan--basic .plan-price,.plan--business .plan-price{top:36px}
  .plan--premium .plan-name{top:12px;left:20px}
  .plan--premium .plan-price{top:36px;left:17px}

  .features{position:absolute;left:20px;right:8px;list-style:none;display:flex;flex-direction:column}
  .features li{display:flex;align-items:center;gap:10px;font-weight:700;font-size:11.4px;line-height:13.6px;min-height:27px}
  .features svg{flex:none;width:24px;height:20px}
  .plan--basic .features{top:90px;gap:16px}
  .plan--premium .features{top:93px;left:16px;gap:10.5px}
  .plan--business .features{top:78px;gap:6.3px}

  .footnote{position:absolute;left:560px;top:978px;font-size:9.2px;line-height:11.5px;color:#333}
  .backfile{position:absolute;left:46px;top:1015px;font-size:17px;line-height:20.5px}
  .contact{position:absolute;right:40px;top:1106px;text-align:right;font-size:14.6px;line-height:17.6px}
  .contact-label{color:#555}
  .contact-line{font-weight:600}
</style>
</head>
<body>
<svg width="0" height="0" style="position:absolute">
  <defs>
    <symbol id="tick" viewBox="0 0 24 20"><path d="M2 11 L9 17 L22 3" fill="none" stroke="var(--tick)" stroke-width="2.6" stroke-linecap="round" stroke-linejoin="round"/></symbol>
  </defs>
</svg>

<main class="flyer">
  <div class="decor decor--top" role="img" aria-label="Decorative cluster of blue and violet geometric triangles"></div>
  <div class="decor decor--bottom" role="img" aria-label="Decorative cluster of blue and violet geometric triangles"></div>

  <div class="brand-ghost" aria-hidden="true">LedgerMint</div>
  <div class="brand">LedgerMint Corp.</div>

  <h1 class="headline">Relax, We’ve<br>Got Your<br>Taxes Covered!</h1>

  <p class="intro intro--lead">It has never been easier to file your taxes.&nbsp; Our <b>virtual tax office</b> let’s you file from the comfort of your <b>home or office</b> and know that our tax expects have taken care of all the work.&nbsp; Completely virtual, forms are signed via <b>SignPad</b> and you can upload documents to us and receive documents from us in our <b>Secured Client Portal</b>.</p>

  <p class="intro intro--meet">Need a <b>tax review</b> or have q<b>uestions</b>? Our tax expects are available on <b>MeetLine, TalkRoom</b> or <b>CallSpace</b> for your convenience.</p>

  <h2 class="pricing-title">Pricing chart</h2>

  <section class="plan plan--basic">
    <div class="plan-name">Basic</div>
    <div class="plan-price">$95</div>
    <ul class="features">
      <li><svg><use href="#tick"/></svg>Full tax preparation from start to finish by a tax expert</li>
      <li><svg><use href="#tick"/></svg>RRSP, donation &amp; medical expenses</li>
      <li><svg><use href="#tick"/></svg>Ideal for newcomers, students &amp; seniors</li>
      <li><svg><use href="#tick"/></svg>Maximum refund guaranteed</li>
      <li><svg><use href="#tick"/></svg>Audit representation (Valued at $30)</li>
    </ul>
  </section>

  <section class="plan plan--business">
    <div class="plan-name">Business</div>
    <div class="plan-price">$195</div>
    <ul class="features">
      <li><svg><use href="#tick"/></svg>Full tax preparation from start to finish by a tax expert</li>
      <li><svg><use href="#tick"/></svg>Business/self-employment income</li>
      <li><svg><use href="#tick"/></svg>Rental Property*</li>
      <li><svg><use href="#tick"/></svg>Partnership income</li>
      <li><svg><use href="#tick"/></svg>Non-resident tax return</li>
      <li><svg><use href="#tick"/></svg>Trust return (T3)</li>
      <li><svg><use href="#tick"/></svg>Audit representation (Valued at $30)</li>
    </ul>
  </section>

  <section class="plan plan--premium">
    <div class="plan-name">Premium</div>
    <div class="plan-price">$125</div>
    <ul class="features">
      <li><svg><use href="#tick"/></svg>Full tax preparation from start to finish by a tax expert</li>
      <li><svg><use href="#tick"/></svg>Emigrant tax terun</li>
      <li><svg><use href="#tick"/></svg>Final (deceased) tax return</li>
      <li><svg><use href="#tick"/></svg>Audit representation (Valued at $30)</li>
      <li><svg><use href="#tick"/></svg>Claim industry specific deductions to lower tax owing</li>
    </ul>
  </section>

  <p class="footnote">* fee includes one rental property or one business schedule.<br>Additional schedules are $145</p>

  <p class="backfile">Have your fallen behind in your taxes? File 3 or more years and receive a 20% discount.<br>We can file back to 2012.</p>

  <address class="contact" style="font-style:normal">
    <div class="contact-label">Contact us:</div>
    <div class="contact-line">hello@ledgermint.ca</div>
    <div class="contact-line">Phone: (877) 555-0148</div>
  </address>
</main>
</body>
</html>
```